Hot Offer banner for product listing page

Hi, we need a banner in the dimensions 210x390px which will be shown in the product listing on our online shop. There are 18 products and in between randomly there should be 3 banners with three different information.
first banner: fast delivery
The idea is to show a stove which is very "fast". Maybe you can make an effect like in Driftcraft Valorne when they activate the warp drive or something similar. Anyway, the banner should indicate that the delivery is very fast for this product.

second banner: Advantage banner
We would like to have a banner which names all our advantages in our online shop. this is the list of advantages:
- over 200,000 satisfied customers
- Best price guarantee
- thousands of devices in stock
- Top ratings

I attached you some examples, just to give you an idea.

```html
<!DOCTYPE html>
<html lang="en">
<head>
<meta charset="utf-8">
<title>Shop banners – Advantages and Fast Delivery</title>
<link rel="stylesheet" href="https://fonts.googleapis.com/css2?family=Anton&family=Montserrat:wght@300&display=swap">
<style>
  :root {
    --backdrop: #ececec;
    --card: #ffffff;
    --orange: #fb8500;
    --orange-soft: #fdb36b;
    --ink: #1d1d1d;
    --red: #ff3a12;
    --warm: #fb8a3a;
    --white: #ffffff;
  }
  html, body {
    margin: 0;
    padding: 0;
    width: 1200px;
    height: 900px;
    overflow: hidden;
    background: var(--backdrop);
  }
  .canvas {
    position: relative;
    width: 1200px;
    height: 900px;
  }
  .banner {
    position: absolute;
    top: 46px;
    width: 432px;
    height: 804px;
    background: var(--card);
    overflow: hidden;
  }
  .banner--advantages { left: 90px; }
  .banner--delivery { left: 676px; }
  .banner svg { display: block; width: 100%; height: 100%; }
  .dot { fill: var(--orange); }
  .icon-area { fill: var(--orange-soft); }
  .advantage {
    font-family: "Anton", "Oswald", sans-serif;
    font-size: 27px;
    fill: var(--ink);
    letter-spacing: 0.2px;
  }
  .headline {
    font-family: "Montserrat", "Helvetica Neue", sans-serif;
    font-weight: 300;
    font-size: 46px;
    fill: var(--white);
    text-anchor: middle;
  }
  .route-arrow { stroke: var(--red); stroke-width: 2; fill: none; }
  .route-icon { fill: var(--red); }
  .stove-area { fill: rgba(255,255,255,0.18); stroke: rgba(255,255,255,0.55); stroke-width: 2; }
</style>
</head>
<body>
<main class="canvas">

  <section class="banner banner--advantages" aria-label="Our advantages">
    <svg viewBox="0 0 360 670" xmlns="http://www.w3.org/2000/svg">
      <circle class="dot" cx="80" cy="72" r="92" role="img" aria-label="Smiling customer emblem"/>
      <circle class="dot" cx="308" cy="50" r="52"/>
      <g role="img" aria-label="Group of customers with a heart">
        <rect class="icon-area" x="278" y="22" width="60" height="58" rx="10"/>
      </g>
      <circle class="dot" cx="285" cy="120" r="12"/>
      <circle class="dot" cx="247" cy="147" r="17" role="img" aria-label="Euro coin"/>
      <circle class="dot" cx="323" cy="172" r="55" role="img" aria-label="Discount badge"/>

      <circle class="dot" cx="180" cy="332" r="155"/>
      <g role="img" aria-label="Stack of cardboard boxes">
        <rect class="icon-area" x="100" y="245" width="160" height="120" rx="14"/>
      </g>

      <circle class="dot" cx="55" cy="482" r="12"/>
      <circle class="dot" cx="187" cy="540" r="22"/>
      <circle class="dot" cx="85" cy="594" r="45"/>
      <g role="img" aria-label="Thumbs up">
        <rect class="icon-area" x="63" y="572" width="44" height="44" rx="8"/>
      </g>
      <circle class="dot" cx="280" cy="600" r="82"/>
      <g role="img" aria-label="Three stars above a group of reviewers">
        <rect class="icon-area" x="218" y="540" width="124" height="110" rx="14"/>
      </g>

      <text class="advantage" x="18" y="77" textLength="164" lengthAdjust="spacingAndGlyphs">Over 200,000</text>
      <text class="advantage" x="18" y="110" textLength="256" lengthAdjust="spacingAndGlyphs">satisfied customers</text>
      <text class="advantage" x="18" y="207" textLength="266" lengthAdjust="spacingAndGlyphs">Best price guarantee</text>
      <text class="advantage" x="18" y="417" textLength="306" lengthAdjust="spacingAndGlyphs">Thousands of devices in</text>
      <text class="advantage" x="18" y="450" textLength="72" lengthAdjust="spacingAndGlyphs">stock</text>
      <text class="advantage" x="18" y="537" textLength="142" lengthAdjust="spacingAndGlyphs">Top ratings</text>
    </svg>
  </section>

  <section class="banner banner--delivery" aria-label="Fast delivery">
    <svg viewBox="0 0 360 670" xmlns="http://www.w3.org/2000/svg">
      <defs>
        <linearGradient id="delivery-glow" x1="0" y1="0" x2="0" y2="1">
          <stop offset="0" stop-color="var(--red)"/>
          <stop offset="1" stop-color="var(--warm)"/>
        </linearGradient>
      </defs>

      <circle cx="182" cy="411" r="349" fill="url(#delivery-glow)"/>

      <g role="img" aria-label="Route from warehouse by truck to the customer's home">
        <rect class="route-icon" x="10" y="70" width="22" height="24" transform="rotate(-18 21 82)"/>
        <path class="route-arrow" d="M67 64 Q88 52 106 58"/>
        <path class="route-arrow" d="M100 53 L107 58 L100 63"/>
        <rect class="route-icon" x="160" y="30" width="46" height="26" rx="4"/>
        <path class="route-arrow" d="M248 50 Q270 50 288 62"/>
        <path class="route-arrow" d="M281 60 L289 63 L286 55"/>
        <rect class="route-icon" x="318" y="74" width="28" height="28"/>
      </g>

      <g role="img" aria-label="Stove rushing forward with speed lines">
        <rect class="stove-area" x="100" y="275" width="160" height="158" rx="6"/>
      </g>

      <text class="headline" x="177" y="574">FAST</text>
      <text class="headline" x="179" y="619">DELIVERY</text>
    </svg>
  </section>

</main>
</body>
</html>
```